Baseball Themed Power Point Template

I am hosting a business meeting in Chicago in July. The audience is a group of young sales professionals.

My meeting needs a generic PowerPoint presentation template with a baseball all-star theme. I have browsed templates for sale on-line and many of them are boring--they show a baseball laying in the grass. None of them have caught my eye.

I would like the template for my meeting to be fun, modern and celebratory. It will only be used once so I don't need a logo or design that needs to have any longevity. The template will be used for an activity that lasts one day only.

As for colors, I would like a red, white and blue color scheme to match the colors of the Dunmore Hawks-- but please don't violate any copyrights. I only attach it for color consideration.

My preferred orientation is 16 by 9. I need a title page, a text page, and a couple color break pages.

I have attached two files--one is the Dunmore Hawks logo so you can match colors. The other is a flyer that interested me because it seemed fun and celebratory.

Target Market(s)

Young professionals, 25-35, sales and marketing. They are fun, competitive and energetic.

Industry/Entity Type

Business

Font styles to use
Sans Serif

Colors
0255a3
ec1f27
ffffff

Requirements
Must have
• Red, white and blue colors. Energy. Modern looking.
Should not have
• Do not violate the Dunmore Hawks logo-I just want to simulate the colors.

```html
<!DOCTYPE html>
<html lang="en">
<head>
<meta charset="utf-8">
<title>Meeting Activities – Slide Ideas</title>
<link rel="stylesheet" href="https://fonts.googleapis.com/css2?family=Roboto+Condensed:wght@300;400&family=Oswald:wght@500&family=Open+Sans:wght@400&display=swap">
<style>
  :root {
    --page-bg: #000000;
    --heading-light: #ffffff;
    --label-grey: #9a9a9a;
    --slide-bg: #ffffff;
    --navy: #0b2a6b;
    --red: #ff0000;
    --ink: #13254a;
    --body-ink: #1c1c1c;
    --bar-blue: #4a7dbf;
    --bar-red: #c0504d;
    --bar-green: #9bbb59;
    --bar-purple: #8064a2;
    --bar-teal: #4bacc6;
  }
  * { box-sizing: border-box; margin: 0; padding: 0; }
  html, body { width: 1200px; height: 1200px; overflow: hidden; background: var(--page-bg); }
  .sheet { position: relative; width: 1200px; height: 1200px; }
  .sheet-title {
    position: absolute; top: 24px; left: 0; width: 1200px; text-align: center;
    font: 300 36px/1 "Roboto Condensed", sans-serif; color: var(--heading-light); letter-spacing: 1px;
  }
  .sheet-note {
    position: absolute; top: 70px; left: 0; width: 1200px; text-align: center;
    font: 400 12px/1 "Roboto Condensed", sans-serif; color: #d8d8d8;
  }
  .slide-label {
    position: absolute; left: 0; width: 1200px; text-align: center;
    font: 400 21px/1 "Roboto Condensed", sans-serif; color: var(--label-grey); letter-spacing: .5px;
  }
  .slide {
    position: absolute; left: 170px; width: 859px; background: var(--slide-bg); overflow: hidden;
  }
  .slide svg.art { position: absolute; inset: 0; width: 100%; height: 100%; }
  .slide-heading { position: absolute; text-align: center; width: 220px; }
  .slide-heading h2 {
    font: 500 28px/1 "Oswald", sans-serif; color: var(--ink); transform: scaleX(.82); letter-spacing: -.3px;
  }
  .slide-heading p { font: 400 11px/1 "Open Sans", sans-serif; color: var(--body-ink); margin-top: 9px; }
  .colour-bar { display: flex; gap: 1px; width: 167px; height: 5px; margin: 13px auto 0; }
  .colour-bar span { flex: 1; }
  .colour-bar .b1 { background: var(--bar-blue); }
  .colour-bar .b2 { background: var(--bar-red); }
  .colour-bar .b3 { background: var(--bar-green); }
  .colour-bar .b4 { background: var(--bar-purple); }
  .colour-bar .b5 { background: var(--bar-teal); }
  .points { position: absolute; width: 320px; list-style: none; }
  .points li { height: 70.5px; }
  .points h3 {
    font: 500 20px/1 "Oswald", sans-serif; color: var(--ink); transform: scaleX(.8); transform-origin: left;
    white-space: nowrap;
  }
  .points p { font: 400 9.4px/13px "Open Sans", sans-serif; color: var(--body-ink); margin-top: 3px; }
</style>
</head>
<body>
<main class="sheet">
  <h1 class="sheet-title">INDIVIDUAL SLIDES FROM PPT DESIGN IDEA - 01 (#11252363)</h1>
  <p class="sheet-note">THE BELOW IDEAS ARE NOT PRESENT IN DESIGN #11252363 DUE TO&nbsp; DISPLAY SPACE ISSUE. BUT STILL THE BELOW SLIDES WIL BE DELIVERED WITH DESIGN #11252363</p>

  <h2 class="slide-label" style="top:112px">MEETING ACTIVITIES&nbsp; SLIDE IDEA - 03</h2>
  <section class="slide" style="top:136px;height:490px">
    <svg class="art" viewBox="0 0 859 490" preserveAspectRatio="none">
      <defs>
        <linearGradient id="field-a" x1="0" y1="0" x2="0.3" y2="1">
          <stop offset="0" stop-color="#7d8a4a"/>
          <stop offset="0.35" stop-color="#8f7a55"/>
          <stop offset="0.7" stop-color="#b5784a"/>
          <stop offset="1" stop-color="#9a5a34"/>
        </linearGradient>
      </defs>
      <polygon role="img" aria-label="Photo: baseball player sliding head-first into a base under stadium lights" fill="url(#field-a)" points="0,0 438,0 234,490 0,490"/>
      <polygon fill="var(--navy)" points="437,0 493,0 373,298 316,298"/>
      <polygon fill="var(--red)" points="501,0 539,0 459,200 421,200"/>
    </svg>
    <div class="slide-heading" style="left:554px;top:62px">
      <h2>MEETING ACTIVITIES</h2>
      <p>Run The Bases</p>
      <div class="colour-bar"><span class="b1"></span><span class="b2"></span><span class="b3"></span><span class="b4"></span><span class="b5"></span></div>
    </div>
    <ul class="points" style="left:504px;top:167px">
      <li><h3>YOUR TEXT HERE</h3><p>Lorem ipsum dolor sit amet, consectetur adipiscing elit. Nunc bibendum eleifend tortor, non porta justo gravida posuere.</p></li>
      <li><h3>YOUR TEXT HERE</h3><p>Lorem ipsum dolor sit amet, consectetur adipiscing elit. Nunc bibendum eleifend tortor, non porta justo gravida posuere.</p></li>
      <li><h3>YOUR TEXT HERE</h3><p>Lorem ipsum dolor sit amet, consectetur adipiscing elit. Nunc bibendum eleifend tortor, non porta justo gravida posuere.</p></li>
      <li><h3>YOUR TEXT HERE</h3><p>Lorem ipsum dolor sit amet, consectetur adipiscing elit. Nunc bibendum eleifend tortor, non porta justo gravida posuere.</p></li>
    </ul>
  </section>

  <h2 class="slide-label" style="top:662px">METING ACTIVITIES&nbsp; SLIDE IDEA - 04</h2>
  <section class="slide" style="top:695px;height:486px">
    <svg class="art" viewBox="0 0 859 486" preserveAspectRatio="none">
      <defs>
        <linearGradient id="field-b" x1="1" y1="0" x2="0.7" y2="1">
          <stop offset="0" stop-color="#7d8a4a"/>
          <stop offset="0.35" stop-color="#8f7a55"/>
          <stop offset="0.7" stop-color="#b5784a"/>
          <stop offset="1" stop-color="#9a5a34"/>
        </linearGradient>
      </defs>
      <polygon role="img" aria-label="Photo: baseball player sliding head-first into a base under stadium lights" fill="url(#field-b)" points="365,0 859,0 859,486 565,486"/>
      <polygon fill="var(--red)" points="262,0 309,0 381,198 342,198"/>
      <polygon fill="var(--navy)" points="310,0 365,0 486,294 429,294"/>
    </svg>
    <div class="slide-heading" style="left:71px;top:60px">
      <h2>MEETING ACTIVITIES</h2>
      <p>Run The Bases</p>
      <div class="colour-bar"><span class="b1"></span><span class="b2"></span><span class="b3"></span><span class="b4"></span><span class="b5"></span></div>
    </div>
    <ul class="points" style="left:20px;top:165px">
      <li><h3>YOUR TEXT HERE</h3><p>Lorem ipsum dolor sit amet, consectetur adipiscing elit. Nunc bibendum eleifend tortor, non porta justo gravida posuere.</p></li>
      <li><h3>YOUR TEXT HERE</h3><p>Lorem ipsum dolor sit amet, consectetur adipiscing elit. Nunc bibendum eleifend tortor, non porta justo gravida posuere.</p></li>
      <li><h3>YOUR TEXT HERE</h3><p>Lorem ipsum dolor sit amet, consectetur adipiscing elit. Nunc bibendum eleifend tortor, non porta justo gravida posuere.</p></li>
      <li><h3>YOUR TEXT HERE</h3><p>Lorem ipsum dolor sit amet, consectetur adipiscing elit. Nunc bibendum eleifend tortor, non porta justo gravida posuere.</p></li>
    </ul>
  </section>
</main>
</body>
</html>
```